Saucy Velvet Kittenz Business Card

We need business cards designed for our consultants to use and hand out to customers.
We are an Adult party plan company (like Crispaboxa but sex toys and lingerie)
We would like bright colours pinks, purples.
The cards need our logo
Space for the reps phone number email address and name.
We need our website on it www.saucyvelvetkittens.com.au

```html
<!DOCTYPE html>
<html lang="en">
<head>
<meta charset="utf-8">
<title>Saucy Velvet Kittenz – Business Card</title>
<link rel="stylesheet" href="https://fonts.googleapis.com/css2?family=Fondamento:ital@1&family=Didact+Gothic&display=swap">
<style>
  :root {
    --page-bg: #2a2a2c;
    --card-purple: #5a2a90;
    --card-magenta: #a3277f;
    --card-pink: #e2227a;
    --silhouette-front: #6a2a8c;
    --silhouette-back: #d8207a;
    --ink: #f4eef6;
  }
  * { box-sizing: border-box; margin: 0; padding: 0; }
  html, body {
    width: 1200px;
    height: 900px;
    overflow: hidden;
    background: var(--page-bg);
  }
  .sheet {
    width: 1200px;
    height: 900px;
    display: flex;
    flex-direction: column;
    align-items: center;
    justify-content: center;
    gap: 48px;
  }
  .card {
    position: relative;
    width: 700px;
    height: 380px;
    overflow: hidden;
    background: linear-gradient(200deg, var(--card-pink) 0%, var(--card-magenta) 50%, var(--card-purple) 100%);
    color: var(--ink);
  }

  .silhouette { position: absolute; }
  .silhouette--back {
    left: 70px; top: 120px; width: 140px; height: 200px;
    background: var(--silhouette-back);
    border-radius: 48% 48% 30% 30%;
  }
  .silhouette--front {
    right: 40px; top: 40px; width: 160px; height: 300px;
    background: var(--silhouette-front);
    border-radius: 45% 45% 25% 35%;
  }

  .website {
    position: absolute;
    left: 240px; top: 250px;
    font-family: "Fondamento", cursive;
    font-style: italic;
    font-size: 28px;
    white-space: nowrap;
  }

  .tagline {
    position: absolute;
    left: 40px; top: 72px;
    font-family: "Fondamento", cursive;
    font-style: italic;
    font-weight: 400;
    font-size: 42px;
    letter-spacing: 2px;
    white-space: nowrap;
  }
  .rep {
    position: absolute;
    left: 210px; top: 140px;
    font-family: "Didact Gothic", sans-serif;
  }
  .rep__name { font-size: 34px; letter-spacing: 1px; }
  .rep__role { font-size: 21px; margin-left: 96px; margin-top: -4px; }
  .contact {
    position: absolute;
    left: 30px; right: 220px; bottom: 40px;
    text-align: right;
    font-family: "Didact Gothic", sans-serif;
    font-size: 25px;
    letter-spacing: 1.5px;
    line-height: 1.55;
    white-space: nowrap;
  }
</style>
</head>
<body>
<main class="sheet">
  <section class="card card--back" aria-label="Card back">
    <div class="silhouette silhouette--back" role="img" aria-label="Silhouette illustration of a little devil girl"></div>
    <p class="website">www.saucyvelvetkittens.com.au</p>
  </section>

  <section class="card card--front" aria-label="Card front">
    <div class="silhouette silhouette--front" role="img" aria-label="Silhouette illustration of a kneeling devil girl with tail"></div>
    <h1 class="tagline">Adult party plan!</h1>
    <div class="rep">
      <p class="rep__name">Sam Carter</p>
      <p class="rep__role">consultants</p>
    </div>
    <div class="contact">
      <p class="contact__phone">0400 555 018</p>
      <p class="contact__email">sam@saucyvelvetkittens.com</p>
    </div>
  </section>
</main>
</body>
</html>
```